We need a book cover design for a fitness professional's guidebook to be a successful trainer. LA celebrity trainer offers 7 ideas that are designed to transform any fitness professional's career and life. The cover design we are into is attached an includes the image of a man who is half dressed in a business suit and half dressed in fitness gear. The back photo should demonstrate the four sphere's the book is designed around (also attached) and will be included on the back with a brief description of the material (included below) and a short bio and photo of the writer (attached) at the very bottom. We'd like the book to have a work book feel, or text book geometry to it. The brand colors are Black and Red. The final design should invoke the feeling of success, health and happiness.

Dimensions: 8 5/8 x 5 3/4

USE WEBSITE AS REFERENCE FOR BRAND COLORS AND DESIGNS:
BrenoVigor.net

BOOK TITLE:
RISING STRIDE
"A fitness professional's guidebook to be a successful trainer."

BACK COVER COPY:
Celebrity conditioning specialist and trainer consultant, Tavo Minardi, offers powerful ideas that are designed to transform every fitness professional's career and life. Reveal essential tools that every trainer and entrepreneur should know. Discover the deeper meaning of yourself and your career by working smarter rather than harder.

Find out how to create a brand, advertise it, and hone in on your market. Create buzz by landing magazine press. How to build celebrity clientele. Explore the world of multi-media projects. And finally, what to do when you reach your goals. This is an opportunity for trainer's to capture a share of the fitness industry’s vast $27B market. Fulfill your fullest earning potential while also understanding what the true meaning of success is, and how to achieve it. Learn what you love to do, what you do well, what the fitness industry needs and what it will pay for.

Aimed at the trainers who want to know the mistakes to avoid, and the habits to establish that will set them apart from the rest, Rising Stride is THE guidebook that has the power to take your career and life in the direction that will prepare you for continued success. Use these business ideas to promote your passive income, generate multiple streams of revenue and increase your investments, resulting in more freedom and access in the fitness industry and beyond. Let Rising Stride unleash your potential to be a successful trainer.

BACK AUTHOR BIO:
Los Angeles based celebrity trainer and trainer consultant, Tavo Minardi, CSCS, developed his very own “Ember” technique and fitness brand. Minardi’s clients include a mix of celebrities, professional athletes, musicians, fashion models, students, political figures and corporate professionals. Kelvo magazine described Minardi’s fitness DVD, TAVOMOVE, as “a workout you’ll look forward to”. Tavo was also the co-developer of a natural energy drink that increases energy and metabolism with an ancient Peruvian super food. Additionally backed by his finance and advertising education, Tavo has consulted several trainers and fitness brands to guide them to their maximum earning potential.

Target Market(s)

Fitness Industry/Trainers

Industry/Entity Type

Advertising

Requirements
Must have
• Consistent with website logo colors, shapes and fonts.

```html
<!DOCTYPE html>
<html lang="en">
<head>
<meta charset="utf-8">
<title>Rising Stride – Book Cover Wrap</title>
<link rel="stylesheet" href="https://fonts.googleapis.com/css2?family=Arimo:wght@400&family=Roboto+Condensed:wght@300;400;500&family=Source+Sans+3:ital,wght@0,400;1,400&display=swap">
<style>
  :root {
    --stage: #c5c3c4;
    --ink: #231f20;
    --band: #231f20;
    --red: #e8453c;
    --red-pale: #f6c7c3;
    --white: #ffffff;
    --body: #2b2b2b;
    --photo-man: linear-gradient(180deg, #c9a07c 0%, #2a2a36 35%, #2f4f9c 60%, #1b1b1b 100%);
    --photo-author: linear-gradient(180deg, #e8b35a 0%, #7b6a5a 45%, #2d2d2d 100%);
  }
  * { margin: 0; padding: 0; box-sizing: border-box; }
  html, body { width: 1200px; height: 1000px; overflow: hidden; background: var(--stage); }
  .canvas { position: relative; width: 1200px; height: 1000px; }
  .wrap {
    position: absolute; left: 28px; top: 90px; width: 1144px; height: 822px;
    background: var(--white); box-shadow: 3px 4px 6px rgba(0,0,0,.35); overflow: hidden;
  }
  .shapes { position: absolute; left: 0; top: 0; }
  .top-band {
    position: absolute; left: 0; top: 0; width: 1144px; height: 120px; background: var(--band);
  }
  .quote {
    position: absolute; left: 20px; top: 16px; width: 520px;
    font: italic 22px/30px "Source Sans 3", sans-serif; color: var(--white); text-align: center;
  }
  .front-title {
    position: absolute; left: 604px; top: 20px; width: 540px; text-align: center;
    font: 300 82px/82px "Roboto Condensed", sans-serif; color: var(--white); letter-spacing: 0;
  }
  .back-copy {
    position: absolute; left: 19px; top: 256px; width: 236px;
    font: 8.6px/11px Arimo, sans-serif; color: var(--body); text-align: justify;
  }
  .back-copy p + p { margin-top: 11px; }
  .back-copy em { font-style: italic; }
  .spheres { position: absolute; left: 10px; top: 600px; }
  .spheres text { font-family: Arimo, sans-serif; }
  .back-rule { position: absolute; left: 268px; top: 255px; width: 1px; height: 553px; background: var(--ink); }
  .back-spine-title {
    position: absolute; left: 282px; top: 255px; height: 462px; width: 80px;
    writing-mode: vertical-rl; transform: rotate(180deg); text-align: center;
    font: 300 72px/80px "Roboto Condensed", sans-serif; color: var(--red-pale);
  }
  .isbn-box {
    position: absolute; left: 280px; top: 725px; width: 87px; height: 82px; border: 1px solid var(--ink);
    display: flex; align-items: center; justify-content: center; text-align: center;
    font: 7px/10px Arimo, sans-serif; color: var(--ink);
  }
  .author-name { position: absolute; left: 375px; top: 250px; font: 400 23px/25px "Source Sans 3", sans-serif; color: var(--red); }
  .author-bio {
    position: absolute; left: 375px; top: 308px; width: 150px;
    font: 8.6px/11px Arimo, sans-serif; color: var(--body); text-align: justify;
  }
  .author-site { position: absolute; left: 375px; top: 594px; font: 9px Arimo, sans-serif; color: var(--red); letter-spacing: 2px; }
  .author-photo { position: absolute; left: 375px; top: 622px; width: 150px; height: 186px; background: var(--photo-author); }
  .spine {
    position: absolute; left: 550px; top: 125px; width: 54px; height: 697px; background: var(--red);
  }
  .spine-title {
    position: absolute; left: 550px; top: 240px; width: 54px; height: 360px;
    writing-mode: vertical-rl; transform: rotate(180deg); text-align: center;
    font: 400 24px/54px Arimo, sans-serif; color: var(--white); letter-spacing: 2px;
  }
  .spine-author {
    position: absolute; left: 550px; top: 628px; width: 54px; height: 180px;
    writing-mode: vertical-rl; transform: rotate(180deg); text-align: center;
    font: 400 15px/54px Arimo, sans-serif; color: var(--white); letter-spacing: 1px;
  }
  .cover-photo { position: absolute; left: 795px; top: 160px; width: 180px; height: 505px; background: var(--photo-man); border-radius: 40px 40px 6px 6px; }
  .subtitle {
    position: absolute; left: 610px; top: 683px; width: 534px; text-align: center;
    font: 400 44px/46px "Roboto Condensed", sans-serif; color: var(--ink);
  }
  .byline {
    position: absolute; left: 610px; top: 780px; width: 534px; text-align: center;
    font: 400 16px Arimo, sans-serif; color: var(--red); letter-spacing: 10px;
  }
</style>
</head>
<body>
<main class="canvas">
  <section class="wrap">
    <svg class="shapes" width="1144" height="822" viewBox="0 0 1144 822" aria-hidden="true">
      <rect x="0" y="125" width="1144" height="697" fill="var(--red)"/>
      <path d="M0,165 C120,170 220,200 272,245 C322,190 430,155 550,150 L550,822 L0,822 Z" fill="var(--white)"/>
      <path d="M604,160 C780,175 1010,300 1144,520 L1144,822 L604,822 Z" fill="var(--white)"/>
    </svg>

    <header class="top-band"></header>
    <p class="quote">“Rising Stride is THE guidebook that has the power to take your career and life in the direction that will prepare you for continued success.”</p>
    <h1 class="front-title">RISING STRIDE</h1>

    <div class="back-copy">
      <p>Celebrity conditioning specialist and trainer consultant, Tavo Minardi, offers powerful business ideas that are designed to transform the fitness professional's career and life. Discover essential strategies that every trainer and entrepreneur should know, and the common mistakes to avoid. Identify the deeper meaning and purpose of your career by working smarter rather than harder.</p>
      <p>Find out how to create a brand, advertise it, and target your market. Create buzz by landing magazine press. Build celebrity clientele. Explore the world of multi-media projects, including TV appearances. Determine what to do when you finally reach your goals. <em>“Rising Stride”</em> is an opportunity for trainers to capture a share of the fitness industry's vast $27 billion market. Reach your highest earning potential, understand your personal definition of success, and learn how to achieve it. Discover what you love to do, what you do well, what the fitness industry needs, and what it will pay for.</p>
      <p>Designed for trainers who want to establish habits that enhance their careers and set them apart from the rest, <em>“Rising Stride”</em> has the power to guide you upwards toward continued success. Use these business ideas to augment your passive income, generate multiple streams of revenue and increase your investments, resulting in more freedom and access in the fitness industry and beyond. Let <em>“Rising Stride”</em> unleash your potential to be a successful trainer.</p>
    </div>

    <svg class="spheres" width="250" height="170" viewBox="0 0 250 170" role="img" aria-label="Four overlapping spheres meeting at success">
      <ellipse cx="78" cy="88" rx="72" ry="40" fill="#f4a58a" fill-opacity=".75" stroke="#999" stroke-width=".6"/>
      <ellipse cx="174" cy="88" rx="72" ry="40" fill="#c8e0b4" fill-opacity=".7" stroke="#999" stroke-width=".6"/>
      <ellipse cx="124" cy="50" rx="50" ry="48" fill="#8cc4ea" fill-opacity=".7" stroke="#999" stroke-width=".6"/>
      <ellipse cx="124" cy="124" rx="50" ry="44" fill="#fbe98e" fill-opacity=".65" stroke="#999" stroke-width=".6"/>
      <text x="124" y="24" font-size="8" text-anchor="middle" fill="#333">What you love</text>
      <text x="40" y="91" font-size="8" text-anchor="middle" fill="#333">What you do well</text>
      <text x="212" y="86" font-size="8" text-anchor="middle" fill="#333">What the world</text>
      <text x="212" y="96" font-size="8" text-anchor="middle" fill="#333">needs</text>
      <text x="124" y="146" font-size="8" text-anchor="middle" fill="#333">What the world</text>
      <text x="124" y="156" font-size="8" text-anchor="middle" fill="#333">will pay for</text>
      <text x="124" y="94" font-size="14" font-weight="bold" text-anchor="middle" fill="#222">SUCCESS</text>
    </svg>

    <div class="back-rule"></div>
    <div class="back-spine-title">RISING STRIDE</div>
    <div class="isbn-box">RESERVED FOR<br>ISBN NUMBER &amp; BARCODE</div>

    <h2 class="author-name">Tavo<br>Minardi, CSCS</h2>
    <p class="author-bio">Hollywood trainer Tavo Minardi, CSCS is a professional fitness consultant and creator of the popular “Ember” technique and brand. His clients include celebrities, pro athletes, musicians, fashion models and political figures. Recognizing his expertise, top publications including Kelvo, Vireo, Pulsar, Home Orbit, Fresh Plate and Star Chatter have featured Minardi as a highly sought-after fitness authority. Kelvo magazine describes his DVD TAVOMOVE as “a workout you'll look forward to.” Minardi appeared on a Norvex commercial aired during the Grand Cup, and he is also the co-developer of a natural energy drink that increases power and metabolism with an ancient Peruvian superfood. Minardi’s fitness expertise is complemented by his education in finance and advertising, and he has guided numerous trainers and brands towards their maximum earning potential.</p>
    <p class="author-site">www.BrenoVigor.net</p>
    <div class="author-photo" role="img" aria-label="Portrait photo of the author at sunset over a city skyline"></div>

    <div class="spine"></div>
    <div class="spine-title">RISING STRIDE</div>
    <div class="spine-author">Tavo Minardi, CSCS</div>

    <div class="cover-photo" role="img" aria-label="Photo of a man walking, half in a business suit with briefcase, half in blue fitness gear"></div>
    <p class="subtitle">THE BUSINESS GUIDEBOOK<br>FOR TRAINER'S SUCCESS</p>
    <p class="byline">TAVO MINARDI, CSCS</p>
  </section>
</main>
</body>
</html>
```